Website - Tides Of Motion

We are catalysts of change in people's lives.
We work with individuals and professionals to bring about instant substantial & transforming change in their lives.
We provide one-on-one lifestyle coaching by an experienced practitioner.
Our existing website is www.tidesofmotion.biz & this site contains our the basis for the content of our desired new project, so please examine this carefully.
We require a professional and captivating website that will instantly impress, engage invite our readers to click & invest their lives.
Our services do not come cheap, but are second to none.
Our website must be contemporary whilst reflecting indisputable class & ultra-confidence in the success of our work.
Target Market(s)
Those who seek to want to change in their lives. Those aged primarily between 30 and 50 years of age, male or female.
Industry/Entity Type
Work

```html
<!DOCTYPE html>
<html lang="en">
<head>
<meta charset="utf-8">
<title>Tides Of Motion — Responsive Website Presentation</title>
<link rel="stylesheet" href="https://fonts.googleapis.com/css2?family=Open+Sans:wght@300;400;600;700&family=Arimo:wght@400&display=swap">
<style>
  :root {
    --lime: #9acb34;
    --lime-dark: #7fae22;
    --ink: #000000;
    --white: #ffffff;
    --orange: #f26a1b;
    --magenta: #d81b5a;
    --rust: #e0672c;
    --caption: #8a8a8a;
    --logo-grey: #b9b9b9;
  }
  * { margin: 0; padding: 0; box-sizing: border-box; }
  html, body { width: 1200px; height: 1000px; overflow: hidden; background: var(--white); }
  body { position: relative; font-family: "Open Sans", Arial, sans-serif; }

  .caption {
    position: absolute;
    font-family: "Arimo", "Helvetica Neue", Arial, sans-serif;
    font-size: 19px; line-height: 25px; color: var(--caption);
  }
  .caption--mobile { left: 18px; top: 29px; width: 400px; }
  .caption--tablet { left: 800px; top: 829px; width: 390px; }

  /* ---------- Mobile screen ---------- */
  .mobile {
    position: absolute; left: 0; top: 146px; width: 437px; height: 836px;
    background: var(--ink); overflow: hidden;
    border-left: 1px solid var(--lime); border-bottom: 3px solid var(--lime);
  }
  .mobile__backdrop {
    position: absolute; inset: 0;
    background:
      linear-gradient(118deg, transparent 0 48%, rgba(110,160,40,.35) 53%, rgba(40,70,20,.2) 58%, transparent 66%),
      radial-gradient(ellipse at 30% 40%, #262626 0%, #111 55%, #050505 100%);
  }
  .mobile__bar {
    position: absolute; left: 0; top: 0; width: 100%; height: 50px; background: var(--lime);
  }
  .menu-button {
    position: absolute; left: 21px; top: 6px; width: 114px; height: 36px;
    border: 1px solid var(--white); color: var(--white);
    font-size: 15px; display: flex; align-items: center; gap: 12px; padding-left: 6px;
  }
  .sound-icon { position: absolute; width: 18px; height: 16px; background: var(--lime); }
  .mobile .sound-icon { left: 0; top: 51px; }

  .logo { position: absolute; display: flex; align-items: center; gap: 12px; }
  .logo__mark { width: 46px; height: 46px; border-radius: 50%; background: var(--lime); }
  .logo__name { font-weight: 400; color: var(--logo-grey); font-size: 22px; line-height: 1.1; }
  .mobile .logo { left: 146px; top: 88px; }
  .mobile .logo__name { width: 110px; }

  .section-title {
    position: absolute; display: flex; align-items: center;
    color: var(--white); border-bottom: 1px solid var(--lime-dark);
  }
  .section-title__flag { background: var(--lime); align-self: stretch; }
  .section-title strong { font-weight: 600; }
  .section-title span { font-weight: 300; }
  .mobile .section-title { left: 69px; top: 198px; width: 300px; height: 36px; font-size: 23px; }
  .mobile .section-title__flag { width: 24px; margin-right: 8px; }

  .intro {
    position: absolute; left: 69px; top: 255px; width: 296px;
    font-size: 12.5px; line-height: 19px; font-weight: 300; color: var(--white);
  }

  .slider { position: absolute; left: 69px; top: 331px; width: 300px; height: 125px; }
  .slider__photo {
    width: 100%; height: 100%;
    background: linear-gradient(180deg, #3a4a5e 0%, #b9c3cc 45%, #e8e6df 60%, #1c1c1c 100%);
  }
  .slider__arrow {
    position: absolute; top: 41px; width: 43px; height: 43px; background: var(--lime);
    display: flex; align-items: center; justify-content: center;
  }
  .slider__arrow--prev { left: 0; opacity: .45; }
  .slider__arrow--next { right: 0; }
  .slider__dots { position: absolute; left: 205px; top: 470px; display: flex; gap: 18px; }
  .slider__dots i { width: 10px; height: 10px; border-radius: 50%; border: 1px solid #888; }
  .slider__dots i.is-active { background: var(--white); border-color: var(--white); }

  .service { position: absolute; left: 69px; width: 292px; color: var(--white); }
  .service--business { top: 524px; }
  .service--individual { top: 687px; }
  .service__icon { float: left; width: 64px; height: 65px; margin-right: 10px; margin-top: 4px; }
  .service__icon--business { background: var(--magenta); }
  .service__icon--individual { background: var(--rust); }
  .service h3 { font-size: 20px; font-weight: 700; line-height: 26px; margin-bottom: 2px; }
  .service p { font-size: 12.5px; line-height: 19px; font-weight: 300; }

  .counter {
    position: absolute; font-weight: 700; color: var(--white); letter-spacing: -1px;
  }
  .counter em { font-style: normal; color: var(--orange); }
  .mobile .counter { left: 2px; top: 794px; font-size: 31px; }
  .expand-icon { position: absolute; width: 18px; height: 18px; background: var(--lime); }
  .mobile .expand-icon { right: 0; bottom: 2px; }

  /* ---------- Tablet screen ---------- */
  .tablet {
    position: absolute; left: 479px; top: 146px; width: 721px; height: 651px;
    background: var(--ink); overflow: hidden;
    border-top: 4px solid var(--lime); border-bottom: 5px solid var(--lime);
  }
  .tablet__backdrop {
    position: absolute; inset: 0;
    background:
      radial-gradient(ellipse 60% 30% at 70% 75%, rgba(60,190,60,.55), transparent 70%),
      linear-gradient(160deg, transparent 40%, rgba(30,120,60,.35) 50%, transparent 58%),
      linear-gradient(180deg, #050808 0%, #0a1410 60%, #03110a 100%);
  }
  .tablet .sound-icon { left: 1px; top: 0; }
  .tablet .logo { left: 452px; top: 26px; }
  .tablet .logo__name { width: 100px; }
  .tablet .section-title { left: 58px; top: 130px; width: 604px; height: 28px; font-size: 18px; }
  .tablet .section-title__flag { width: 18px; margin-right: 8px; }

  .menu-tab {
    position: absolute; left: 1px; top: 279px; width: 34px; height: 84px; background: #0d0d0d;
    border-left: 3px solid var(--lime);
  }
  .menu-tab span {
    position: absolute; left: 50%; top: 50%; transform: translate(-50%, -50%) rotate(-90deg);
    color: var(--white); font-size: 20px;
  }

  .work-tile { position: absolute; width: 226px; height: 146px; }
  .work-tile--sunset { background: linear-gradient(180deg, #6b6fa8 0%, #c98aa0 45%, #e8a050 70%, #3a2a3a 100%); }
  .work-tile--lake { background: linear-gradient(180deg, #1e2f6a 0%, #5672b8 40%, #243f7c 70%, #0a1a3c 100%); }
  .tablet .work-tile--a { left: 58px; top: 217px; }
  .tablet .work-tile--b { left: 325px; top: 217px; }
  .stack .work-tile { box-shadow: 0 0 6px rgba(0,0,0,.6); }
  .stack .s1 { left: 40px; top: 456px; transform: rotate(4deg); }
  .stack .s2 { left: 20px; top: 385px; transform: rotate(4deg); }
  .stack .s3 { left: 66px; top: 392px; transform: rotate(-6deg); }
  .stack .s4 { left: 58px; top: 403px; }

  .tablet .counter { left: 1px; top: 608px; font-size: 28px; }
  .tablet .expand-icon { right: 2px; bottom: 2px; }
</style>
</head>
<body>

  <p class="caption caption--mobile">Example of how the site looks on a mobile device.<br>The menu panel at the top is fixed as the page scrolls down for easy navigation</p>

  <section class="mobile">
    <div class="mobile__backdrop" role="img" aria-label="Dark textured backdrop crossed by a green swoosh"></div>

    <header class="mobile__bar">
      <div class="menu-button">
        <svg width="22" height="18" viewBox="0 0 22 18" aria-hidden="true">
          <g fill="#fff"><rect x="0" y="0" width="5" height="4"/><rect x="7" y="0" width="15" height="4"/><rect x="0" y="7" width="5" height="4"/><rect x="7" y="7" width="15" height="4"/><rect x="0" y="14" width="5" height="4"/><rect x="7" y="14" width="15" height="4"/></g>
        </svg>
        Menu
      </div>
    </header>
    <div class="sound-icon"></div>

    <div class="logo"><span class="logo__mark"></span><span class="logo__name">Tides of Motion</span></div>

    <h2 class="section-title"><i class="section-title__flag"></i><strong>About us</strong>&nbsp;<span>// Yes we can.</span></h2>

    <p class="intro">At Tides Of Motion, our Master Practitioner will inspire you, shifting your perspective &amp; facilitating your mind with the freedom to realise your dreams.</p>

    <div class="slider">
      <div class="slider__photo" role="img" aria-label="Photo of a person with arms raised against a cloudy sky"></div>
      <span class="slider__arrow slider__arrow--prev"></span>
      <span class="slider__arrow slider__arrow--next">
        <svg width="10" height="16" viewBox="0 0 10 16" aria-hidden="true"><path d="M2 1 L9 8 L2 15" fill="none" stroke="#fff" stroke-width="1.5"/></svg>
      </span>
    </div>
    <div class="slider__dots"><i class="is-active"></i><i></i><i></i></div>

    <article class="service service--business">
      <div class="service__icon service__icon--business" role="img" aria-label="Business service emblem"></div>
      <h3>Business</h3>
      <p>Tides Of Motion have worked with CEO's &amp; business owners throughout Australia, as catalysts to their outstanding success. We will facilitate &amp; oversee your development of better and more effective ways of increasing performance and improving effectiveness.</p>
    </article>

    <article class="service service--individual">
      <div class="service__icon service__icon--individual" role="img" aria-label="Individual service emblem"></div>
      <h3>Individual</h3>
      <p>Tides Of Motion works every day with people just like you who wish to change their lives.<br>Mum's &amp; Dads experiencing marriage problems or who find themselves suddenly single, teenagers who have experienced death of someone close or</p>
    </article>

    <div class="counter">01/<em>01</em></div>
    <div class="expand-icon"></div>
  </section>

  <section class="tablet">
    <div class="tablet__backdrop" role="img" aria-label="Dark backdrop with glowing green light waves"></div>
    <div class="sound-icon"></div>

    <div class="logo"><span class="logo__mark"></span><span class="logo__name">Tides of Motion</span></div>

    <h2 class="section-title"><i class="section-title__flag"></i><strong>Showcase work</strong>&nbsp;<span>here// The clean, responsive way.</span></h2>

    <div class="menu-tab"><span>menu</span></div>

    <div class="work-tile work-tile--sunset work-tile--a" role="img" aria-label="Sunset photo with an inspirational quote about a new day"></div>
    <div class="work-tile work-tile--lake work-tile--b" role="img" aria-label="Photo of a person sitting before a mountain lake"></div>

    <div class="stack">
      <div class="work-tile work-tile--lake s1" role="img" aria-label="Lake photo in a scattered stack"></div>
      <div class="work-tile work-tile--sunset s2" role="img" aria-label="Sunset quote photo in a scattered stack"></div>
      <div class="work-tile work-tile--sunset s3" role="img" aria-label="Sunset quote photo in a scattered stack"></div>
      <div class="work-tile work-tile--sunset s4" role="img" aria-label="Sunset photo with an inspirational quote, top of the stack"></div>
    </div>

    <div class="counter">02/<em>01</em></div>
    <div class="expand-icon"></div>
  </section>

  <p class="caption caption--tablet">Example of how the site looks on a tablet device.<br>The images resize automatically</p>

</body>
</html>
```